Pell Clinic Standing Banner

Design a standing banner for a community health care clinic. Our website is www.pellclinic.org. On there you can find our list of services. I have uploaded our logo, mission/vision/about us statements, as well as our business cards for contact information and so you have an idea of the theme we are going for.
Our tagline is building a healthier society.

We want the banner to showcase our name, tagline, services, and the contact methods listed on the business card except for the address.

```html
<!DOCTYPE html>
<html lang="en">
<head>
<meta charset="utf-8">
<title>Pell Clinic Standing Banner</title>
<link href="https://fonts.googleapis.com/css2?family=Montserrat:wght@300;500&family=Roboto+Condensed:wght@400;700&family=Roboto:wght@500;700&display=swap" rel="stylesheet">
<style>
  :root {
    --green: #5cb94a;
    --red: #e0282a;
    --ink: #222222;
    --ink-soft: #333333;
    --white: #ffffff;
    --backdrop: #ececec;
    --veg: #8cc63f;
  }
  * { margin: 0; padding: 0; box-sizing: border-box; }
  html, body { width: 680px; height: 1200px; overflow: hidden; background: var(--backdrop); }
  .banner {
    position: absolute; left: 93px; top: 0; width: 494px; height: 1200px;
    background: var(--white); overflow: hidden;
    font-family: "Roboto Condensed", sans-serif; color: var(--ink);
  }
  .header-band { position: absolute; left: 0; top: 0; width: 494px; height: 280px; }
  .brand-mark {
    position: absolute; left: 182px; top: 36px; width: 130px; height: 130px;
    border-radius: 50%; background: var(--red);
  }
  .brand-name {
    position: absolute; left: 0; right: 0; top: 172px; text-align: center;
    font-family: "Montserrat", sans-serif; font-weight: 500; font-size: 50px;
    color: var(--white); line-height: 60px;
  }
  .center { position: absolute; left: 0; right: 0; text-align: center; }
  .tagline { top: 302px; font-weight: 700; font-size: 28px; color: var(--green); line-height: 34px; }
  .section-title { font-weight: 700; font-size: 24px; color: var(--red); line-height: 28px; }
  .mission-title { top: 346px; }
  .vision-title { top: 456px; }
  .statement { font-size: 16px; line-height: 20px; color: var(--ink); padding: 0 40px; }
  .mission-text { top: 380px; }
  .vision-text { top: 491px; }
  .services-title {
    top: 612px; font-family: "Roboto", sans-serif; font-weight: 700;
    font-size: 54px; line-height: 62px; color: var(--red);
  }
  .service { position: absolute; display: flex; align-items: center; }
  .service-icon { width: 56px; height: 56px; flex: none; }
  .service-label {
    font-family: "Roboto", sans-serif; font-weight: 500; font-size: 25px;
    line-height: 30px; color: var(--ink-soft); margin-left: 14px;
  }
  .nutrition-art {
    width: 64px; height: 48px; flex: none;
    background: radial-gradient(circle at 50% 60%, var(--veg), var(--green) 70%);
    border-radius: 8px 8px 32px 32px;
  }
  .invite-lead { top: 962px; font-size: 16px; line-height: 20px; }
  .invite-call { top: 1007px; font-size: 23px; line-height: 28px; }
  .invite-note { top: 1034px; font-size: 14px; line-height: 17px; }
  .footer-band {
    position: absolute; left: 0; top: 1065px; width: 494px; height: 135px; background: var(--green);
  }
  .phone { top: 1084px; font-size: 35px; line-height: 42px; color: var(--white); }
  .web-row {
    position: absolute; left: 0; right: 0; top: 1140px; height: 24px;
    display: flex; align-items: center; justify-content: center; gap: 14px;
  }
  .web-rule { flex: 1; height: 2px; background: var(--white); }
  .web-address {
    font-family: "Montserrat", sans-serif; font-weight: 300; font-size: 19px;
    letter-spacing: 4px; color: var(--white);
  }
</style>
</head>
<body>
<main class="banner">
  <svg class="header-band" viewBox="0 0 494 280" aria-hidden="true">
    <polygon points="0,0 494,0 494,207 247,276 0,207" fill="var(--green)"/>
  </svg>
  <div class="brand-mark" aria-hidden="true"></div>
  <h1 class="brand-name">Pell Clinic</h1>

  <h2 class="center tagline">BUILDING A HEALTHIER SOCIETY</h2>

  <h3 class="center section-title mission-title">MISSION</h3>
  <p class="center statement mission-text">Pell Clinic provides nonprofit, holistic healthcare services to underserved populations in Greater Houston, working toward the ambitious goal of comprehensive healing for all.</p>

  <h3 class="center section-title vision-title">VISION</h3>
  <p class="center statement vision-text">The vision of Pell Clinic focuses on a healthier Houston where anyone/everyone can access quality comprehensive healthcare services. We envision a community unified in the spirit of humanity and shares the goal of enhancing human lives to build a healthier society.</p>

  <h2 class="center services-title">SERVICES</h2>

  <div class="service" style="left:36px;top:696px;">
    <svg class="service-icon" viewBox="0 0 56 56" aria-hidden="true">
      <rect x="18" y="8" width="20" height="10" rx="2" fill="none" stroke="var(--red)" stroke-width="4"/>
      <rect x="2" y="16" width="52" height="34" rx="4" fill="var(--red)"/>
      <rect x="23" y="22" width="10" height="22" fill="var(--green)"/>
      <rect x="17" y="28" width="22" height="10" fill="var(--green)"/>
    </svg>
    <span class="service-label">HEALTH<br>FAIRS</span>
  </div>
  <div class="service" style="left:240px;top:696px;">
    <svg class="service-icon" viewBox="0 0 56 56" aria-hidden="true">
      <path d="M28 52 L6 28 A13 13 0 0 1 28 12 A13 13 0 0 1 50 28 Z" fill="var(--red)"/>
      <path d="M28 52 L9 31 H20 L24 23 L29 40 L33 31 H47 Z" fill="var(--green)"/>
      <polyline points="4,31 20,31 24,23 29,40 33,31 52,31" fill="none" stroke="var(--white)" stroke-width="2.5"/>
    </svg>
    <span class="service-label">COMMUNITY<br>CLINIC</span>
  </div>
  <div class="service" style="left:36px;top:770px;">
    <svg class="service-icon" viewBox="0 0 56 56" aria-hidden="true">
      <path d="M20 6 H36 M23 6 V22 L8 48 H48 L33 22 V6" fill="none" stroke="var(--red)" stroke-width="4" stroke-linejoin="round"/>
      <path d="M14 38 H42 L46 46 H10 Z" fill="var(--green)"/>
      <circle cx="27" cy="28" r="2" fill="var(--green)"/>
      <circle cx="31" cy="22" r="1.5" fill="var(--green)"/>
    </svg>
    <span class="service-label">LAB</span>
  </div>
  <div class="service" style="left:240px;top:770px;">
    <svg class="service-icon" viewBox="0 0 56 56" aria-hidden="true">
      <line x1="10" y1="10" x2="22" y2="22" stroke="var(--ink-soft)" stroke-width="2"/>
      <rect x="20" y="18" width="28" height="10" transform="rotate(45 34 23)" fill="var(--green)"/>
      <line x1="44" y1="40" x2="52" y2="48" stroke="var(--red)" stroke-width="5"/>
      <circle cx="6" cy="6" r="3" fill="var(--red)"/>
    </svg>
    <span class="service-label">SUBSTANCE<br>ABUSE</span>
  </div>
  <div class="service" style="left:36px;top:862px;">
    <svg class="service-icon" viewBox="0 0 56 56" aria-hidden="true">
      <rect x="22" y="4" width="10" height="24" rx="3" transform="rotate(-25 27 16)" fill="var(--green)"/>
      <path d="M14 30 A16 16 0 0 0 40 44" fill="none" stroke="var(--green)" stroke-width="5"/>
      <rect x="10" y="46" width="36" height="6" fill="var(--green)"/>
      <rect x="24" y="30" width="12" height="5" fill="var(--green)"/>
    </svg>
    <span class="service-label">CLINICAL<br>RESEARCH</span>
  </div>
  <div class="service" style="left:240px;top:866px;">
    <div class="nutrition-art" role="img" aria-label="Bowl of fresh vegetables and fruit"></div>
    <span class="service-label" style="margin-left:10px;">NUTRITION</span>
  </div>

  <p class="center invite-lead">If you share the same ambition and desire to<br>make quality holistic health care accessible,</p>
  <p class="center invite-call">we invite you to join us!</p>
  <p class="center invite-note">Volunteer, donate, or talk to us about how you can further this shared vision.</p>

  <div class="footer-band"></div>
  <p class="center phone">(555) 014-2290</p>
  <div class="web-row">
    <span class="web-rule"></span>
    <span class="web-address">www.pellclinic.org</span>
    <span class="web-rule"></span>
  </div>
</main>
</body>
</html>
```